Varneck Law Business cards and stationary design project

We are looking for a stationary design for business cards (double sided), 8x10, 5x7, and legal and standard envelopes.

We would like the design to match the logo that we have already.
Color palate preferred is Teal, White, grey and any others that will look good for a professional law firm.

We would like this statement: "RELATIONSHIPS. RESPECT. RESULT" to be on the back of the business cards and maybe on the stationary if it looks good.

Please see link to website for more information: www.varneck-law-example.com

Target Market(s)

Potential clients that need Attorney services.

Industry/Entity Type

Law Firm

Contact Information for Business Card

We would like the front and back to be two different colors. Current business cards are teal front, grey back and are a vertical design. We are open to options with colors.

Font styles to use
Serif

Colors
33a6d7
33b8a4
b9b9b9
5c5c5c

Requirements
Must have
• Logo supplied needs to go on the card and stationary.
• Match website color palate, www.varneck-law-example.com
• Be professional and not too wordy.
• Criminal Law, Civil Litigation, Personal Injury, Restraining Orders need to be on the card.
Nice to have
• RELATIONSHIPS. RESPECT. RESULTS. on the back of the card.
Should not have
• Not be too busy/wordy or too flashy.

```html
<!DOCTYPE html>
<html lang="en">
<head>
<meta charset="utf-8">
<title>Varneck Law – Business Card</title>
<link rel="stylesheet" href="https://fonts.googleapis.com/css2?family=Source+Sans+3:wght@400;600;700&display=swap">
<style>
  :root {
    --backdrop-top: #2b2b2b;
    --backdrop-bottom: #050505;
    --card-white: #ffffff;
    --card-grey: #b9b9b9;
    --teal: #177f8c;
    --ink: #111111;
    --on-grey: #ffffff;
  }
  * { margin: 0; padding: 0; box-sizing: border-box; }
  html, body { width: 1200px; height: 900px; overflow: hidden; }
  body {
    position: relative;
    background: linear-gradient(180deg, var(--backdrop-top) 0%, #1a1a1a 55%, var(--backdrop-bottom) 100%);
    font-family: "Source Sans 3", "Myriad Pro", Arial, sans-serif;
  }
  .card {
    position: absolute;
    top: 170px;
    width: 347px;
    height: 561px;
    text-align: center;
  }
  .card-front { left: 259px; background: var(--card-white); }
  .card-back { left: 641px; background: var(--card-grey); }

  .line { position: absolute; left: 0; right: 0; white-space: nowrap; }

  .firm-name {
    font-weight: 600;
    font-size: 32px;
    letter-spacing: 1px;
    line-height: 1;
  }
  .card-front .firm-name { top: 134px; color: var(--teal); }
  .card-back .firm-name { top: 412px; color: var(--on-grey); }
  .firm-mark {
    display: inline-block;
    width: 12px; height: 12px;
    background: var(--teal);
    margin-right: 10px;
    vertical-align: 4px;
  }

  .person-name { top: 218px; font-size: 21px; font-weight: 600; color: var(--teal); }
  .person-role { top: 242px; font-size: 15px; color: var(--ink); }

  .contact { font-size: 15px; color: var(--ink); line-height: 18px; }
  .contact svg { width: 11px; height: 11px; fill: var(--teal); vertical-align: -1px; margin-right: 3px; }
  .contact-phone { top: 297px; }
  .contact-fax { top: 320px; }
  .contact-email { top: 343px; }
  .contact-web { top: 366px; }

  .address { font-size: 15px; color: var(--ink); line-height: 19px; }
  .address-street { top: 406px; }
  .address-country { top: 424px; }

  .practice { font-size: 15px; font-weight: 600; color: var(--teal); line-height: 20px; }
  .practice-1 { top: 463px; }
  .practice-2 { top: 484px; }
  .practice-3 { top: 504px; }

  .tagline {
    top: 496px;
    font-size: 17px;
    font-weight: 600;
    color: var(--on-grey);
    letter-spacing: 0.2px;
  }
</style>
</head>
<body>

  <section class="card card-front" aria-label="Business card front">
    <div class="line firm-name"><span class="firm-mark"></span>Varneck Law</div>

    <div class="line person-name">Jonathan Smith</div>
    <div class="line person-role">Managing Director</div>

    <div class="line contact contact-phone">
      <svg viewBox="0 0 12 12"><path d="M2.4 0.6 4.3 2.5 3.2 4a7 7 0 0 0 4.8 4.8l1.5-1.1 1.9 1.9-1.3 1.8C5 11 1 7 0.6 1.9z"/></svg>(044)-456-7890
    </div>
    <div class="line contact contact-fax">
      <svg viewBox="0 0 12 12"><path d="M3 0h5v3H3zM1 4h10v6H9v2H3v-2H1zM4 8v3h4V8z"/></svg>123-456-7890
    </div>
    <div class="line contact contact-email">
      <svg viewBox="0 0 12 12"><path d="M0 2h12v8H0zM1 3l5 4 5-4z" fill-rule="evenodd"/></svg>info@youremail.com
    </div>
    <div class="line contact contact-web">
      <svg viewBox="0 0 12 12"><circle cx="6" cy="6" r="6"/></svg>www.website.com
    </div>

    <div class="line address address-street">12345, Address Goes Here</div>
    <div class="line address address-country">Country Name, 123456</div>

    <div class="line practice practice-1">Practice areas, Criminal Law,</div>
    <div class="line practice practice-2">Civil Litigation/Personal Injury</div>
    <div class="line practice practice-3">Restraining Orders</div>
  </section>

  <section class="card card-back" aria-label="Business card back">
    <div class="line firm-name">Varneck Law</div>
    <div class="line tagline">RELATIONSHIPS. RESPECT. RESULT</div>
  </section>

</body>
</html>
```